Tidewell Gin - Label for new Gin bottle

I am looking for a bottle label for our small batch, handcrafted Gin. We are located in the bay-side city of Frankston (Victoria, Australia). I know I want more of a serious label but am torn between traditional or modern styling.

Label to include;
• Tidewell GIN (name)
• Hand Crafted
• Small Batch
• 40% Vol

Using 700ml MERIDA Spirit Bottle - Cork

Requirements
Must have
• Name; Tidewell Gin
Method: Hand Crafted
Batch Size; Small Batch
Alc; 40% Vol
Nice to have
• Maybe a coastal/seaside reference or reference to distilling.

```html
<!DOCTYPE html>
<html lang="en">
<head>
<meta charset="utf-8">
<title>Tidewell Gin – Label Variants</title>
<link rel="stylesheet" href="https://fonts.googleapis.com/css2?family=Antonio:wght@100;200&family=Montserrat:wght@300;400;700;800&display=swap">
<style>
  :root {
    --paper: #ffffff;
    --sky: #67afd1;
    --mist: #d3e8f3;
    --ink-black: #000000;
    --ink-teal: #336683;
  }
  html, body {
    margin: 0;
    padding: 0;
    width: 1200px;
    height: 1200px;
    overflow: hidden;
    background: var(--paper);
  }
  .label-sheet {
    display: block;
    width: 1200px;
    height: 1200px;
  }
  .label-body { fill: url(#body-tone); stroke: var(--ink); stroke-width: 10; }
  .diamond-outer { fill: var(--sky); stroke: var(--ink); stroke-width: 8; stroke-linejoin: miter; }
  .diamond-inner { fill: var(--paper); stroke: var(--ink); stroke-width: 7; }
  .badge-ring { fill: var(--paper); stroke: var(--ink); stroke-width: 11; }
  .badge-art { fill: var(--sky); stroke: var(--ink); stroke-width: 5; }
  .foot-art { fill: var(--paper); stroke: var(--ink); stroke-width: 5; }
  .rule { stroke: var(--ink); stroke-width: 5; }
  .method {
    font-family: "Montserrat", sans-serif;
    font-weight: 700;
    font-size: 33px;
    letter-spacing: 1.5px;
    fill: var(--ink);
  }
  .batch {
    font-family: "Montserrat", sans-serif;
    font-weight: 300;
    font-size: 22px;
    letter-spacing: 1.5px;
    fill: var(--ink);
  }
  .brand-name {
    font-family: "Montserrat", sans-serif;
    font-weight: 800;
    font-size: 88px;
    letter-spacing: 3px;
    fill: var(--ink);
  }
  .spirit {
    font-family: "Antonio", sans-serif;
    font-weight: 100;
    font-size: 272px;
    fill: var(--ink);
  }
  .strength {
    font-family: "Montserrat", sans-serif;
    font-weight: 400;
    font-size: 20px;
    letter-spacing: 1px;
    fill: var(--ink);
  }
  .variant-black { --ink: var(--ink-black); }
  .variant-teal { --ink: var(--ink-teal); }
</style>
</head>
<body>
<svg class="label-sheet" viewBox="0 0 1930 1930" xmlns="http://www.w3.org/2000/svg">
  <defs>
    <linearGradient id="body-tone" x1="0" y1="0" x2="0" y2="1">
      <stop offset="0" stop-color="#d3e8f3"/>
      <stop offset="0.58" stop-color="#c4e0ee"/>
      <stop offset="0.66" stop-color="#67afd1"/>
      <stop offset="1" stop-color="#67afd1"/>
    </linearGradient>
    <path id="method-arc" d="M 300,916 A 690,690 0 0 1 666,916"/>

    <symbol id="gin-label" viewBox="0 0 965 1930" width="965" height="1930" overflow="visible">
      <path class="label-body" role="img" aria-label="Wave scale pattern above, rolling sea waves and diagonal stripes below"
            d="M75,690 Q75,665 100,655 L483,450 L866,655 Q893,665 893,690 L893,1290 Q893,1305 878,1312 L500,1510 Q483,1518 466,1510 L88,1312 Q75,1305 75,1290 Z"/>

      <path class="foot-art" role="img" aria-label="Trident emblem over a rising half sun"
            d="M403,1478 A80,80 0 0 1 563,1478 L500,1510 Q483,1518 466,1510 Z"/>

      <polygon class="diamond-outer" points="25,1027 483,758 940,1027 483,1428"/>
      <polygon class="diamond-inner" points="70,1030 483,784 895,1030 483,1396"/>

      <circle class="badge-ring" cx="484" cy="612" r="155"/>
      <circle class="badge-art" cx="484" cy="612" r="125" role="img" aria-label="Copper pot still with porthole and coiled pipe"/>

      <text class="method" text-anchor="middle"><textPath href="#method-arc" startOffset="50%">HAND - CRAFTED</textPath></text>
      <text class="batch" x="483" y="923" text-anchor="middle">SMALL - BATCH</text>
      <text class="brand-name" x="483" y="1008" text-anchor="middle" textLength="515" lengthAdjust="spacingAndGlyphs">TIDEWELL</text>
      <text class="spirit" x="478" y="1280" text-anchor="middle" textLength="205" lengthAdjust="spacingAndGlyphs">GIN</text>
      <line class="rule" x1="245" y1="1147" x2="345" y2="1147"/>
      <line class="rule" x1="613" y1="1147" x2="713" y2="1147"/>
      <text class="strength" x="483" y="1330" text-anchor="middle">40% VOL</text>
    </symbol>
  </defs>

  <use class="variant-black" href="#gin-label" x="0" y="0"/>
  <use class="variant-teal" href="#gin-label" x="965" y="0"/>
</svg>
</body>
</html>
```